Yacht, Boats, Watersports company needs a redesign of business card

Hello Designers!
We are a Boat dealership company that sells fun in the water, we sell boats, Yachts, Kayaks and also yacht WaterSport toys. We are looking to redesign our business cards in to something a little bit more sophisticated. in a way that we can make better use of our company colors. I'm attaching a zipped file containing the company 3 sets of company logo which one is an horizontal another one is a vertical and also a chromed 3d logo. Also is included two set of business cards that we use and also some designs that i think it's interesting. We use PMS 2026c Orange and PMS 7687C Blue. I would like to see at least two different options with the orange as accent and also using blue as an accent color. It's really important for the business cards to have a font option and size that is legible to most people. Our current website is wwww.corvellamarine.com. Please visit if you want to have a better feeling of the Boat dealership
You can send Single sided or double side options. We are now using single sided but we may be open for a double side option if we really like the design.
Target Market(s)
Marine, boat sales, yacht sales, water toys sales/
Contact Information for Business Card
Name: Dale Pritchett
Address: 718 West Halden Lane,
Dania Beach, FL 33019
Phone: 954-382-7146
Fax: 954:382-7139
Cell: 954-451-8320
Email: 212@corvellamarine.com
Website: corvellamarine.com
Requirements
Must have
- the current information of the business card provided.
logo
use the PMS Colors
Nice to have
- a touch of elegance and sophistication but simple
Should not have
- should not have any typography that is hard to read, the card should be simple but yet sophisticated.

```html
<!DOCTYPE html>
<html lang="en">
<head>
<meta charset="utf-8">
<title>Corvella Marine — Business Card</title>
<link href="https://fonts.googleapis.com/css2?family=Lexend:wght@400;500&display=swap" rel="stylesheet">
<style>
  :root {
    --navy: #252f4b;
    --orange: #f39c23;
    --white: #ffffff;
    --page: #ffffff;
  }
  html, body {
    margin: 0;
    padding: 0;
    overflow: hidden;
  }
  body {
    width: 842px;
    height: 1200px;
    background: var(--page);
    position: relative;
    font-family: "Lexend", sans-serif;
  }
  .card {
    position: absolute;
    top: 182px;
    width: 263px;
    height: 431px;
    display: block;
  }
  .card--front { left: 98px; }
  .card--back { left: 481px; }
  .fill-navy { fill: var(--navy); }
  .fill-orange { fill: var(--orange); }
  .brand-name {
    font-family: "Lexend", sans-serif;
    font-weight: 500;
    fill: var(--orange);
    font-size: 15px;
    letter-spacing: 1.5px;
  }
  .brand-name--vertical {
    fill: var(--navy);
    font-size: 20px;
    letter-spacing: 1px;
  }
  .person-name {
    font-family: "Lexend", sans-serif;
    font-weight: 400;
    fill: var(--white);
    font-size: 20px;
    letter-spacing: 0.5px;
  }
  .contact-text {
    font-family: "Lexend", sans-serif;
    font-weight: 400;
    fill: var(--white);
    font-size: 9.5px;
    letter-spacing: 0.2px;
  }
  .icon-box { fill: var(--orange); }
  .icon-glyph { fill: var(--navy); }
  .icon-line { fill: none; stroke: var(--navy); stroke-width: 1.2; }
  .brand-ring { fill: none; stroke: var(--navy); stroke-width: 4; }
</style>
</head>
<body>

  <!-- Front: contact side -->
  <svg class="card card--front" viewBox="0 0 263 431" xmlns="http://www.w3.org/2000/svg" aria-label="Business card front">
    <rect class="fill-navy" x="0" y="0" width="263" height="431"/>
    <polygon class="fill-orange" points="61.7,0 263,0 201.8,80.5"/>
    <polygon class="fill-orange" points="166,431 232.6,392 263,431"/>

    <g class="brand">
      <text class="brand-name" x="41" y="104">CORVELLA</text>
      <text class="brand-name" x="41" y="123">MARINE</text>
    </g>

    <text class="person-name" x="40" y="207">DALE PRITCHETT</text>

    <g class="contact-list">
      <!-- address -->
      <rect class="icon-box" x="40.5" y="232" width="20" height="20"/>
      <path class="icon-glyph" d="M50.5 236.5a4 4 0 0 1 4 4c0 3-4 7.5-4 7.5s-4-4.5-4-7.5a4 4 0 0 1 4-4z"/>
      <circle class="icon-box" cx="50.5" cy="240.5" r="1.4"/>
      <text class="contact-text" x="76" y="239">718 West Halden Lane,</text>
      <text class="contact-text" x="76" y="252">Dania Beach, FL 33019</text>

      <!-- phone -->
      <rect class="icon-box" x="40.5" y="259" width="20" height="20"/>
      <path class="icon-glyph" d="M44 266.5c0-2 13-2 13 0v1.5h-3v-1.2h-7v1.2h-3z"/>
      <path class="icon-glyph" d="M46.5 269h8l1.5 5h-11z"/>
      <text class="contact-text" x="76" y="272.5">954-382-7146</text>

      <!-- fax -->
      <rect class="icon-box" x="40.5" y="287" width="20" height="20"/>
      <rect class="icon-glyph" x="46.5" y="290.5" width="8" height="3"/>
      <rect class="icon-glyph" x="44" y="294" width="13" height="6.5" rx="1"/>
      <rect class="icon-box" x="47" y="297.5" width="7" height="1"/>
      <rect class="icon-glyph" x="46.5" y="299" width="8" height="4.5"/>
      <rect class="icon-box" x="48" y="300.5" width="5" height="0.8"/>
      <rect class="icon-box" x="48" y="302" width="5" height="0.8"/>
      <text class="contact-text" x="76" y="300">954:382-7139</text>

      <!-- cell -->
      <rect class="icon-box" x="40.5" y="314" width="20" height="20"/>
      <path class="icon-glyph" d="M46 317.5l2.5-.5 1.5 3.5-1.6 1.2c.7 1.8 1.9 3.2 3.6 4.2l1.3-1.5 3.4 1.6-.6 2.5c-5.5-.5-9.8-5.2-10.1-11z"/>
      <text class="contact-text" x="76" y="327.5">954-451-8320</text>

      <!-- email -->
      <rect class="icon-box" x="40.5" y="342" width="20" height="20"/>
      <path class="icon-glyph" d="M45 346.5l5.5 5.5 5.5-5.5v11h-11z"/>
      <text class="contact-text" x="76" y="355.5">212@corvellamarine.com</text>

      <!-- web -->
      <rect class="icon-box" x="40.5" y="369" width="20" height="20"/>
      <circle class="icon-line" cx="50.5" cy="379" r="6"/>
      <ellipse class="icon-line" cx="50.5" cy="379" rx="2.6" ry="6"/>
      <line class="icon-line" x1="44.5" y1="379" x2="56.5" y2="379"/>
      <line class="icon-line" x1="45.5" y1="376" x2="55.5" y2="376"/>
      <line class="icon-line" x1="45.5" y1="382" x2="55.5" y2="382"/>
      <text class="contact-text" x="76" y="383">corvellamarine.com</text>
    </g>
  </svg>

  <!-- Back: brand side -->
  <svg class="card card--back" viewBox="0 0 263 431" xmlns="http://www.w3.org/2000/svg" aria-label="Business card back">
    <rect class="fill-orange" x="0" y="0" width="263" height="431"/>
    <polygon class="fill-navy" points="0,0 200.7,0 61,80.5"/>
    <polygon class="fill-navy" points="0,431 30.3,392 97.2,431"/>

    <circle class="brand-ring" cx="131" cy="114" r="24"/>
    <text class="brand-name brand-name--vertical" transform="translate(124 162) rotate(90)">CORVELLA MARINE</text>
  </svg>

</body>
</html>
```